Unique Home Cooking School needs Wordpress Design

We need a wordpress design for our small business based in Singapore called Twirly Pebbles. It is a unique cooking school where the cooking course menu is completely customised to our client's preference/lifestyle/requests. More information can be found on our site: twirlypebbles.com

We are looking for something simple and easy to navigate. We are currently using a free template which we have customised ourselves. As the business is growing, we are looking to have a site more suited to our needs. The site should also be photo friendly, as we often post up photos of our food. It should also be social media integrated as a lot of our business is driven by QV.

The look and feel should really reflect the personalities of both owners - like the logo. Please feel free to contact us if you need more clarification.

Target Market(s)

Our target audience are usually female, with children, aged 25 - 45.
They are either stay-at-home mums or full-time mums that are keen to do more for the family.

Industry/Entity Type

Small Business

Requirements
Must have
• The wordpress design has to be able to accommodate food photos on every page.
It also needs to be able to support social media feeds within the site.
Should not have
• Design should not have any chef-like design elements as we are not chefs. We are two stay-home-mums wanting to impart skills to other stay-home-mums or domestic helpers.

```html
<!DOCTYPE html>
<html lang="en">
<head>
<meta charset="utf-8">
<title>Twirly Pebbles – Cooking Lessons for Everyone</title>
<link rel="stylesheet" href="https://fonts.googleapis.com/css2?family=Source+Sans+3:ital,wght@0,400;0,600;1,400;1,600&display=swap">
<style>
  :root {
    --pink: #f58fca;
    --pink-bar: #f59bd0;
    --teal: #14897b;
    --ink: #2b2b2b;
    --text: #4a4a4a;
    --muted: #5c5c5c;
    --icon: #3d3d3d;
    --band: #f1f1f1;
    --white: #ffffff;
  }
  * { box-sizing: border-box; margin: 0; padding: 0; }
  html, body { width: 1200px; height: 1000px; overflow: hidden; background: var(--white); }
  body { font-family: "Source Sans 3", "Source Sans Pro", sans-serif; color: var(--text); position: relative; }

  .top-bar { height: 4px; background: var(--pink-bar); }

  .site-header { position: relative; height: 108px; background: #fbfbfb; }
  .brand { position: absolute; left: 104px; top: 34px; display: flex; align-items: center; gap: 8px; }
  .brand-dot { width: 14px; height: 14px; border-radius: 50%; background: var(--pink); }
  .brand-name { font-size: 22px; font-weight: 600; color: var(--ink); }

  .main-nav { position: absolute; top: 52px; left: 0; }
  .main-nav a { position: absolute; font-size: 14px; color: var(--ink); text-decoration: none; white-space: nowrap; letter-spacing: .2px; }
  .main-nav a.current { font-weight: 600; }
  .main-nav a.current::after { content: ""; position: absolute; left: -5px; right: -5px; top: 22px; height: 3px; background: var(--pink); }

  .contact { position: absolute; right: 105px; top: 38px; text-align: center; }
  .contact-label { color: var(--teal); font-size: 14px; font-weight: 600; }
  .contact-numbers { color: var(--ink); font-size: 14px; margin-top: 3px; }
  .phone-icon { position: absolute; left: 860px; top: 42px; }

  .hero { position: relative; height: 421px; }
  .hero-photo { position: absolute; inset: 0; background: linear-gradient(90deg, #6b5a4a 0%, #4a3f36 30%, #c08a4a 50%, #d9a86a 65%, #c9c0b5 80%, #3f5a30 100%); }
  .hero-caption { position: absolute; left: 121px; top: 0; width: 395px; height: 421px; background: rgba(0,0,0,.62); color: var(--white); text-align: center; }
  .hero-title { font-size: 30px; font-style: italic; font-weight: 600; text-align: left; padding: 104px 0 0 23px; }
  .hero-text { font-size: 14px; font-weight: 600; line-height: 21px; padding: 8px 18px 0; }
  .hero-dots { position: absolute; top: 308px; left: 164px; display: flex; gap: 11px; }
  .hero-dots span { width: 9px; height: 9px; border-radius: 50%; background: var(--white); }
  .hero-dots span.active { background: var(--pink); }
  .hero-arrows { position: absolute; left: 344px; top: 360px; width: 52px; height: 36px; border-radius: 18px 18px 0 0; background: rgba(0,0,0,.55); }

  .menus { height: 303px; text-align: center; }
  .section-lead { font-size: 24px; font-style: italic; font-weight: 400; color: var(--ink); padding-top: 10px; letter-spacing: -.2px; }
  .section-lead em, .welcome-title em { color: var(--pink); font-style: italic; }
  .menu-list { display: flex; justify-content: center; gap: 50px; margin-top: 20px; }
  .menu-card { width: 300px; }
  .menu-icon { height: 84px; display: flex; align-items: flex-end; justify-content: center; }
  .menu-title { color: var(--pink); font-size: 18px; font-weight: 400; margin-top: 6px; }
  .menu-text { font-size: 13px; font-weight: 600; line-height: 21px; color: var(--muted); margin-top: 6px; hyphens: auto; -webkit-hyphens: auto; }

  .welcome { background: var(--band); height: 164px; padding: 13px 97px 0 103px; }
  .welcome-title { text-align: center; font-size: 24px; font-style: italic; font-weight: 400; color: var(--ink); }
  .welcome-text { font-size: 13px; font-weight: 600; line-height: 23px; color: var(--muted); text-align: justify; margin-top: 14px; hyphens: auto; -webkit-hyphens: auto; }
</style>
</head>
<body>
  <div class="top-bar"></div>

  <header class="site-header">
    <div class="brand"><span class="brand-dot"></span><span class="brand-name">Twirly Pebbles</span></div>
    <nav class="main-nav">
      <a class="current" href="#" style="left:345px">HOME</a>
      <a href="#" style="left:424px">ABOUT US</a>
      <a href="#" style="left:528px">COURSES</a>
      <a href="#" style="left:627px">BLOG</a>
      <a href="#" style="left:703px">CONTACT US</a>
    </nav>
    <svg class="phone-icon" width="38" height="34" viewBox="0 0 38 34" aria-hidden="true">
      <path d="M8 2 L13 9 L10 13 C12 19 16 23 22 26 L26 22 L33 27 L29 32 C16 31 4 19 3 6 Z" fill="var(--pink)"/>
      <path d="M18 6 C24 7 28 11 29 17 M18 1 C27 2 33 8 34 17" stroke="var(--pink)" stroke-width="2" fill="none"/>
    </svg>
    <div class="contact">
      <div class="contact-label">SMS / ChatLine / Call Us:</div>
      <div class="contact-numbers">+65.8000.1234 / +65.9000.5678</div>
    </div>
  </header>

  <section class="hero">
    <div class="hero-photo" role="img" aria-label="Photo of a cooking class: students seated watching an instructor demonstrate at a stove"></div>
    <div class="hero-caption">
      <h1 class="hero-title">Lorem ipsum dolor sit amet,</h1>
      <p class="hero-text">Lorem ipsum dolor sit amet, consectetuer adipiscing elit. Aenean commodo ligula eget dolor. Aenean massa. Cum sociis natoque penatibus et magnis dis parturient montes, nascetur ridiculus mus. Donec quam felis, ultricies nec, pellentesque eu, pretium quis, sem. Nulla consequat massa quis enim.</p>
      <div class="hero-dots"><span></span><span class="active"></span><span></span><span></span></div>
      <div class="hero-arrows">
        <svg width="52" height="36" viewBox="0 0 52 36" aria-hidden="true">
          <path d="M22 12 L16 18 L22 24 M30 12 L36 18 L30 24" stroke="#fff" stroke-width="3" fill="none"/>
        </svg>
      </div>
    </div>
  </section>

  <section class="menus">
    <h2 class="section-lead">Here are a few sample menus that we have customised as per <em>our customers’ request.</em></h2>
    <div class="menu-list">
      <article class="menu-card">
        <div class="menu-icon">
          <svg width="82" height="82" viewBox="0 0 82 82" aria-hidden="true">
            <path d="M3 46 H79 V80 H3 Z M11 54 V72 H71 V54 Z" fill="var(--icon)" fill-rule="evenodd"/>
            <path d="M14 52 A27 27 0 0 1 68 52 M21 52 A20 20 0 0 1 61 52 M28 52 A13 13 0 0 1 54 52" stroke="var(--icon)" stroke-width="4" fill="none"/>
            <path d="M64 44 L82 33" stroke="var(--icon)" stroke-width="5"/>
            <path d="M38 2 C34 8 42 10 38 16 M46 4 C42 10 50 12 46 18" stroke="var(--icon)" stroke-width="2" fill="none"/>
          </svg>
        </div>
        <h3 class="menu-title">Sample Customised Menu 1</h3>
        <p class="menu-text">We developed this menu for our client who was looking for cooking lessons for her new helper.&nbsp; Our client and her husband work full-time and entrusted the running of the household to their helper.</p>
      </article>
      <article class="menu-card">
        <div class="menu-icon">
          <svg width="78" height="72" viewBox="0 0 78 72" aria-hidden="true">
            <path d="M0 22 H78 C76 38 60 48 39 48 C18 48 2 38 0 22 Z" fill="var(--icon)"/>
            <path d="M20 44 L10 70 M58 44 L68 70 M22 58 H56" stroke="var(--icon)" stroke-width="6" fill="none"/>
            <path d="M28 2 C24 8 32 10 28 16 M39 2 C35 8 43 10 39 16 M50 2 C46 8 54 10 50 16" stroke="var(--icon)" stroke-width="3" fill="none"/>
          </svg>
        </div>
        <h3 class="menu-title">Sample Customised Menu 2</h3>
        <p class="menu-text">We developed this menu for our client who was looking for cooking lessons for her new helper.&nbsp; Our client and her husband work full-time and entrusted the running of the household to their helper.</p>
      </article>
      <article class="menu-card">
        <div class="menu-icon">
          <svg width="72" height="72" viewBox="0 0 72 72" aria-hidden="true">
            <path d="M10 30 H62 V60 C62 66 58 70 52 70 H20 C14 70 10 66 10 60 Z" fill="var(--icon)"/>
            <path d="M6 26 H66 V31 H6 Z M2 38 H10 V46 H2 Z M62 38 H70 V46 H62 Z M30 18 H42 V24 H30 Z" fill="var(--icon)"/>
            <path d="M26 2 C22 7 30 9 26 14 M36 2 C32 7 40 9 36 14 M46 2 C42 7 50 9 46 14" stroke="var(--icon)" stroke-width="3" fill="none"/>
          </svg>
        </div>
        <h3 class="menu-title">Sample Customised Menu 3</h3>
        <p class="menu-text">We developed this menu for our client who was looking for cooking lessons for her new helper.&nbsp; Our client and her husband work full-time and entrusted the running of the household to their helper.</p>
      </article>
    </div>
  </section>

  <section class="welcome">
    <h2 class="welcome-title">Welcome to <em>Twirly Pebbles</em></h2>
    <p class="welcome-text">We are two very Twirly Pebbles who share a passion for cooking and eating different foods, trying out new eateries and the love for collecting cookbooks! We believe that eating well and being able to provide our young families with delicious, healthy meals made at home is the foundation to general well-being.&nbsp; Since being Mums and whenever possible we try to make a lot from scratch to ensure only good things go into our children’s bodies. From mushy baby foods, to healthy sweet or savoury snacks to enticing meals that will interest them enough to eat it!</p>
  </section>
</body>
</html>
```